Tolvik cards

I want a simple business card that pops.
Logo on one side.
On side two i want.
"Are you thinking about a new building on your property, or renovating an existing structure? Contact".....
Owners Name: Gary Pellman
Owners Phone number: 555-209-4176
Address:4716 Copper Fern RD, Harlow Springs, OH 43987
Committed to Quality, Service, and Integrity

```html
<!DOCTYPE html>
<html lang="en">
<head>
<meta charset="utf-8">
<title>Tolvik Builders – Business Cards</title>
<link rel="stylesheet" href="https://fonts.googleapis.com/css2?family=Arimo:ital,wght@0,400;0,700;1,700&display=swap">
<style>
  :root {
    --backdrop: #5b5b5b;
    --card-white: #ffffff;
    --brown-dark: #4a2f1c;
    --brown-text: #5a3a25;
    --grey-text: #555555;
    --divider: #cfcfcf;
  }
  * { margin: 0; padding: 0; box-sizing: border-box; }
  html, body {
    width: 1200px; height: 1200px; overflow: hidden;
    background: var(--backdrop);
    font-family: "Arimo", Arial, sans-serif;
  }
  .card {
    position: absolute;
    width: 689px; height: 393px;
    left: 266px;
    overflow: hidden;
  }
  .card--front { top: 158px; background: var(--card-white); }
  .card--back {
    top: 652px;
    background: radial-gradient(ellipse at 50% 45%, #9b836a 0%, #7a6048 45%, #563923 100%);
  }

  .front__question {
    position: absolute; top: 34px; left: 0; width: 100%;
    text-align: center;
    font-style: italic; font-weight: 700;
    font-size: 19px; line-height: 24px;
    color: var(--brown-text);
  }
  .brand {
    position: absolute;
    display: flex; align-items: center; gap: 10px;
    font-weight: 700; color: var(--brown-dark);
    letter-spacing: 1px; white-space: nowrap;
  }
  .brand__square { display: block; background: currentColor; }
  .front__brand { left: 194px; top: 215px; transform: translate(-50%, -50%); font-size: 42px; }
  .front__brand .brand__square { width: 28px; height: 28px; }

  .front__divider {
    position: absolute; left: 319px; top: 134px;
    width: 1px; height: 164px; background: var(--divider);
  }
  .contact { position: absolute; left: 352px; top: 148px; color: var(--grey-text); }
  .contact__name {
    font-weight: 700; font-size: 30px; line-height: 34px; color: var(--brown-dark);
    margin-bottom: 14px;
  }
  .contact__phone { display: flex; align-items: center; gap: 10px; font-size: 16.5px; line-height: 20px; margin-bottom: 12px; }
  .contact__phone svg { width: 15px; height: 15px; fill: var(--brown-dark); }
  .contact__address { font-size: 16.5px; line-height: 21px; }

  .front__band { position: absolute; left: 0; bottom: 0; width: 689px; height: 33px; }
  .front__motto {
    position: absolute; right: 30px; bottom: 7px;
    font-size: 15.5px; color: #ffffff; white-space: nowrap;
  }

  .back__brand {
    left: 50%; top: 46%; transform: translate(-50%, -50%);
    font-size: 74px; color: #e9dccb; gap: 18px;
  }
  .back__brand .brand__square { width: 48px; height: 48px; }
</style>
</head>
<body>
  <section class="card card--front">
    <p class="front__question">Are you thinking about a new building on your property,<br>or renovating an existing structure?</p>

    <div class="brand front__brand"><span class="brand__square"></span>TOLVIK</div>

    <div class="front__divider"></div>

    <div class="contact">
      <p class="contact__name">GARY PELLMAN</p>
      <p class="contact__phone">
        <svg viewBox="0 0 24 24" aria-hidden="true"><path d="M6.6 10.8a15.1 15.1 0 0 0 6.6 6.6l2.2-2.2a1 1 0 0 1 1-.25 11.4 11.4 0 0 0 3.6.57 1 1 0 0 1 1 1V20a1 1 0 0 1-1 1A17 17 0 0 1 3 4a1 1 0 0 1 1-1h3.5a1 1 0 0 1 1 1c0 1.25.2 2.45.57 3.57a1 1 0 0 1-.25 1z"/></svg>
        555-209-4176
      </p>
      <p class="contact__address">4716 Copper Fern RD<br>Harlow Springs, OH 43987</p>
    </div>

    <svg class="front__band" viewBox="0 0 689 33" preserveAspectRatio="none" aria-hidden="true">
      <defs>
        <linearGradient id="stripGrad" x1="0" x2="1">
          <stop offset="0" stop-color="#7a5e45"/>
          <stop offset="0.55" stop-color="#a89078"/>
          <stop offset="1" stop-color="#6e5238"/>
        </linearGradient>
      </defs>
      <rect x="0" y="17" width="320" height="16" fill="url(#stripGrad)"/>
      <polygon points="305,33 333,0 689,0 689,33" fill="var(--brown-dark)"/>
      <polygon points="302,33 330,0 333,0 305,33" fill="#ffffff"/>
    </svg>
    <p class="front__motto">Committed to Quality, Service, and Integrity</p>
  </section>

  <section class="card card--back">
    <div class="brand back__brand"><span class="brand__square"></span>TOLVIK</div>
  </section>
</body>
</html>
```